Business Card Design Project

Our organization is in need of a business card design with the use of our logo. We are looking for professional design that will embellish the image our consulting firm.

Here is a summary of what we do: Quorvent is systems consulting firm that specializes in the management, migration, and maintenance of IT infrastructure solutions.

Here is a link to my website: http://quorvent-example.com

I have attached the logo.

Target Market(s)

Organization that need IT and server support.

Industry/Entity Type

Business

```html
<!DOCTYPE html>
<html lang="en">
<head>
<meta charset="utf-8">
<title>Quorvent Business Card</title>
<link rel="stylesheet" href="https://fonts.googleapis.com/css2?family=Maven+Pro:wght@400;500;700&display=swap">
<style>
  :root {
    --page-bg: #e6e6e6;
    --card-white: #ffffff;
    --brand-navy: #2a3866;
    --brand-orange: #f07a2a;
    --brand-orange-dark: #d9621b;
    --card-dark: #2b2b2d;
    --card-dark-deep: #202022;
    --text-light: #f2f2f2;
    --icon-glyph: #2b2b2d;
  }
  * { box-sizing: border-box; margin: 0; padding: 0; }
  html, body {
    width: 1200px;
    height: 861px;
    overflow: hidden;
  }
  body {
    background: var(--page-bg);
    font-family: "Maven Pro", sans-serif;
    position: relative;
  }
  .business-card {
    position: absolute;
    left: 150px;
    top: 173px;
    width: 900px;
    height: 515px;
    border-radius: 28px;
    overflow: hidden;
    background: var(--card-white);
    box-shadow: 0 12px 30px rgba(0,0,0,0.25);
  }
  .card-header {
    position: relative;
    height: 240px;
    background: var(--card-white);
    display: flex;
    align-items: center;
    padding-left: 110px;
  }
  .brand-mark {
    width: 110px;
    height: 110px;
    border-radius: 50%;
    background: var(--brand-navy);
    flex: none;
  }
  .brand-divider {
    width: 5px;
    height: 160px;
    background: var(--brand-orange);
    margin: 0 38px 0 48px;
    flex: none;
  }
  .brand-name {
    font-size: 78px;
    font-weight: 400;
    color: var(--brand-navy);
    letter-spacing: 1px;
    line-height: 1;
  }
  .accent-band {
    height: 18px;
    background: linear-gradient(180deg, var(--brand-orange), var(--brand-orange-dark));
  }
  .card-body {
    position: relative;
    height: 257px;
    background: linear-gradient(180deg, var(--card-dark), var(--card-dark-deep));
    padding: 38px 56px 0 52px;
    display: flex;
    justify-content: space-between;
    align-items: flex-start;
  }
  .contact-list {
    list-style: none;
    display: flex;
    flex-direction: column;
    gap: 14px;
    flex: none;
  }
  .contact-item {
    display: flex;
    align-items: center;
    gap: 16px;
    color: var(--text-light);
    font-size: 27px;
    font-weight: 400;
    letter-spacing: 0.4px;
    line-height: 1;
    white-space: nowrap;
    height: 36px;
  }
  .contact-icon {
    width: 36px;
    height: 36px;
    flex: none;
  }
  .employee {
    text-align: right;
    padding-top: 2px;
    flex: none;
    white-space: nowrap;
  }
  .employee-name {
    color: var(--brand-orange);
    font-size: 36px;
    font-weight: 500;
    line-height: 1.1;
  }
  .employee-title {
    color: var(--text-light);
    font-size: 24px;
    font-weight: 700;
    margin-top: 2px;
  }
</style>
</head>
<body>
  <article class="business-card">
    <header class="card-header">
      <div class="brand-mark" aria-hidden="true"></div>
      <div class="brand-divider" aria-hidden="true"></div>
      <h1 class="brand-name">quorvent</h1>
    </header>
    <div class="accent-band" aria-hidden="true"></div>
    <section class="card-body">
      <ul class="contact-list">
        <li class="contact-item">
          <svg class="contact-icon" viewBox="0 0 36 36" aria-hidden="true">
            <circle cx="18" cy="18" r="18" fill="var(--brand-orange)"/>
            <path d="M11 25 l3-3 a2 2 0 0 1 2 0 l2 2 l6-6 l-2-2 a2 2 0 0 1 0-2 l3-3 a1.5 1.5 0 0 1 2 0 l1 1 c1 3-2 9-6 13 s-10 7-13 6 l-1-1 a1.5 1.5 0 0 1 0-2z" fill="var(--icon-glyph)"/>
          </svg>
          <span>123-456-7890</span>
        </li>
        <li class="contact-item">
          <svg class="contact-icon" viewBox="0 0 36 36" aria-hidden="true">
            <circle cx="18" cy="18" r="18" fill="var(--brand-orange)"/>
            <rect x="13" y="8" width="10" height="20" rx="2" fill="var(--icon-glyph)"/>
            <rect x="15" y="11" width="6" height="5" fill="var(--brand-orange)"/>
            <rect x="15" y="18" width="6" height="7" fill="var(--brand-orange)" opacity="0.6"/>
          </svg>
          <span>123-456-7890</span>
        </li>
        <li class="contact-item">
          <svg class="contact-icon" viewBox="0 0 36 36" aria-hidden="true">
            <circle cx="18" cy="18" r="18" fill="var(--brand-orange)"/>
            <rect x="8" y="11" width="20" height="14" rx="1.5" fill="var(--icon-glyph)"/>
            <path d="M9 12 L18 19 L27 12" stroke="var(--brand-orange)" stroke-width="1.6" fill="none"/>
          </svg>
          <span>employee@quorvent-example.com</span>
        </li>
        <li class="contact-item">
          <svg class="contact-icon" viewBox="0 0 36 36" aria-hidden="true">
            <circle cx="18" cy="18" r="18" fill="var(--brand-orange)"/>
            <rect x="8" y="10" width="20" height="14" rx="1.5" fill="var(--icon-glyph)"/>
            <rect x="10" y="12" width="16" height="10" fill="var(--brand-orange)"/>
            <rect x="13" y="25" width="10" height="2" fill="var(--icon-glyph)"/>
          </svg>
          <span>quorvent-example.com</span>
        </li>
      </ul>
      <div class="employee">
        <p class="employee-name">Employee Name</p>
        <p class="employee-title">Title</p>
      </div>
    </section>
  </article>
</body>
</html>
```